Homepage design for female-owned English/French speaking Law firm

Brief Update - we prefer not to have a photo of a person in the hero shot

Corvell.com.au is the website for a English/French Bilingual Female-owned Law Firm, Morillaqua Corvell.
Overall Design notes:
Professional, yet warm and welcoming
Historic foundations but Progressive, woman-owned, sleek, innovative and modern.
Approachable, casual yet professional. Sans-serif font and light colours would help this
2 languages switched by flags (English/French)

Winner must provide
Home page design
Standard (inner) page design (can be provided after winner is selected)
All photos used in the design without charge
Updates

Requirements
Should not have
• Update - we prefer not to have a photo of a person in the hero shot

```html
<!DOCTYPE html>
<html lang="en">
<head>
<meta charset="utf-8">
<title>Morillaqua Corvell Solicitors</title>
<link rel="stylesheet" href="https://fonts.googleapis.com/css2?family=Playfair+Display:wght@400;700&family=Poppins:wght@400;500;600&family=Roboto:wght@400;500;700&family=Rubik:wght@500&display=swap">
<style>
:root{
  --orange:#f7891f;
  --hero-bg:#fdeae0;
  --ink:#333333;
  --text:#7a7a7a;
  --line:#d9d9d9;
  --footer:#474747;
  --white:#ffffff;
}
*{margin:0;padding:0;box-sizing:border-box}
html,body{width:1200px;height:3110px;overflow:hidden}
body{position:relative;background:var(--white);font-family:'Poppins',sans-serif;color:var(--text)}
.abs{position:absolute}
.serif{font-family:'Playfair Display',serif;color:var(--ink);font-weight:700}
.btn{position:absolute;display:flex;align-items:center;justify-content:center;background:var(--orange);color:var(--white);border-radius:20px;font-family:'Roboto',sans-serif;font-weight:500;font-size:14px;text-transform:uppercase}
.eyebrow{font-family:'Roboto',sans-serif;color:var(--orange);font-size:16px;line-height:20px;font-weight:500;text-transform:uppercase}
.read-more{position:absolute;font-family:'Roboto',sans-serif;font-weight:700;font-size:12px;color:var(--orange);display:flex;align-items:center;gap:8px}

/* header */
.topline{top:0;left:0;width:1200px;height:3px;background:var(--orange)}
.site-header{top:3px;left:0;width:1200px;height:75px;background:var(--white)}
.brand{position:absolute;left:160px;top:24px;display:flex;align-items:center;gap:10px}
.brand-mark{width:14px;height:14px;background:var(--orange)}
.brand-name{font-family:'Poppins',sans-serif;font-weight:500;font-size:20px;line-height:28px;color:var(--ink);white-space:nowrap}
.main-nav{position:absolute;top:33px;left:702px;display:flex;font-family:'Roboto',sans-serif;font-size:11px;color:#777}
.main-nav span{margin-right:28px}
.main-nav .active{color:var(--orange);font-weight:500}

/* hero */
.hero{top:78px;left:0;width:1200px;height:444px;background:var(--hero-bg);overflow:hidden}
.hero-art{position:absolute;left:560px;top:55px;width:640px;height:389px;border-radius:220px 0 0 0;background:radial-gradient(ellipse at 55% 60%,#fbe2d4 0%,#f6d2bf 55%,#f3c8ae 100%)}
.hero-kicker{left:160px;top:140px;font-size:22px;line-height:26px;font-weight:400}
.hero-title{left:159px;top:164px;font-size:48px;line-height:58px;letter-spacing:0.5px}
.hero-copy{left:157px;top:230px;width:345px;font-family:'Roboto',sans-serif;font-size:12.5px;line-height:19px;color:#777}

/* about */
.about-back{left:144px;top:754px;width:234px;height:260px;background:var(--orange);border-radius:14px}
.about-photo{left:160px;top:612px;width:391px;height:388px;border-radius:12px;background:linear-gradient(135deg,#f3f0ec 0%,#d7cdbf 45%,#7b6a57 75%,#4a3a2c 100%);box-shadow:0 4px 14px rgba(0,0,0,.15)}
.about-title{left:605px;top:624px;font-size:34px;line-height:44px}
.about-copy{left:605px;top:677px;width:435px;font-size:12.3px;line-height:18.8px;text-align:justify}
.check-list{left:605px;top:848px;list-style:none;font-size:12.5px;font-weight:600;color:#666}
.check-list li{display:flex;align-items:center;gap:9px;height:22.5px}

/* features */
.feature{position:absolute;top:1076px;width:262px}
.feature svg{display:block}
.feature h3{font-family:'Playfair Display',serif;font-weight:400;font-size:12.5px;line-height:16px;color:var(--ink);text-transform:uppercase;margin-top:21px}
.feature p{font-size:11.3px;line-height:15.7px;margin-top:9px}
.feature .read-more{position:static;margin-top:15px}

/* practice */
.practice{top:1316px;left:0;width:1200px;height:513px;background:linear-gradient(180deg,#ffffff 0%,#f2f2f2 30%,#ededed 100%)}
.practice-center{position:absolute;left:0;width:1200px;text-align:center}
.practice-title{font-size:34px;line-height:44px}
.area-card{position:absolute;top:1474px;width:280px}
.area-photo{width:280px;height:210px;border-radius:10px}
.area-card h4{font-family:'Playfair Display',serif;font-weight:700;font-size:15px;line-height:20px;color:var(--ink);margin-top:12px}
.area-card .read-more{position:static;margin-top:10px;font-size:11px;opacity:.85}

/* stats */
.stats-shadow{left:152px;top:1796px;width:262px;height:90px;background:#666}
.stats{left:160px;top:1774px;width:880px;height:101px;background:var(--white);box-shadow:0 2px 10px rgba(0,0,0,.12);display:flex;align-items:center}
.stat{padding-left:35px;padding-right:28px;border-right:1px solid var(--line);height:55px}
.stat:nth-child(4){border-right:none}
.stat b{display:block;font-family:'Rubik',sans-serif;font-weight:500;font-size:36px;line-height:36px;color:var(--ink)}
.stat span{font-family:'Roboto',sans-serif;font-size:12px;color:#888}
.view-more{position:absolute;right:14px;top:15px;width:137px;height:86px;background:var(--orange);color:var(--white);display:flex;align-items:center;justify-content:center;font-family:'Roboto',sans-serif;font-weight:700;font-size:20px}

/* history */
.history-title{left:160px;top:2030px;font-size:34px;line-height:44px}
.history-copy{left:160px;top:2084px;width:508px;font-size:11.6px;line-height:15.8px;text-align:justify}
.history-copy p{margin-bottom:15.5px}
.history-back{left:760px;top:2022px;width:280px;height:293px;background:linear-gradient(135deg,#f39a3c,#e9821c);border-radius:0 0 44px 0}
.history-photo{left:717px;top:2001px;width:252px;height:335px;background:linear-gradient(160deg,#c7bcae 0%,#8a7866 45%,#2d2a2c 100%)}

/* contact */
.contact-card{left:160px;top:2519px;width:314px;height:322px;background:var(--orange);border-radius:40px 0 0 40px;color:var(--white);font-family:'Roboto',sans-serif}
.contact-item{position:absolute;left:28px;display:flex;gap:12px}
.contact-item strong{display:block;font-weight:500;font-size:15px;text-transform:uppercase}
.contact-item small{display:block;font-size:11.5px;font-weight:700;line-height:17px;margin-top:2px;padding-left:2px}
.form-intro{left:515px;top:2525px;width:525px;font-family:'Roboto',sans-serif;font-size:13.5px;line-height:17px;color:#888}
.field-label{position:absolute;font-family:'Roboto',sans-serif;font-size:10.5px;color:#888}
.field{position:absolute;border:1px solid var(--line);background:var(--white)}

/* footer */
.footer{top:2928px;left:0;width:1200px;height:132px;background:var(--footer)}
.social{position:absolute;top:2954px;left:512px;display:flex;gap:8px}
.social span{width:38px;height:38px;border:1.5px solid var(--white);border-radius:50%}
.footer-nav{position:absolute;top:3014px;left:0;width:1200px;display:flex;justify-content:center;font-family:'Roboto',sans-serif;font-weight:500;font-size:11px;color:var(--white)}
.footer-nav span{margin:0 21px}
.footer-nav .active{color:var(--orange)}
.legal{top:3060px;left:0;width:1200px;height:50px;background:var(--orange);color:var(--white);font-family:'Roboto',sans-serif;font-size:10px;display:flex;align-items:center;justify-content:center}
</style>
</head>
<body>

<div class="abs topline"></div>
<header class="abs site-header">
  <div class="brand">
    <span class="brand-mark"></span>
    <span class="brand-name">Morillaqua Corvell</span>
  </div>
  <nav class="main-nav">
    <span class="active">Home</span><span>Our Services</span><span style="margin-left:12px">Download</span><span>Contact us</span><span>Links</span>
  </nav>
</header>

<section class="abs hero">
  <div class="hero-art" role="img" aria-label="Illustration of a classical courthouse with scales of justice, books and a briefcase"></div>
  <h2 class="abs serif hero-kicker">OUR SMALL,</h2>
  <h1 class="abs serif hero-title">SKILLED TEAM</h1>
  <p class="abs hero-copy">Lorem ipsum dolor sit amet, consectetur adipiscing elit. Sed tincidunt nisi a turpis interdum consequat. Pellentesque ut semper ex. Morbi mauris ipsum, efficitur .</p>
  <div class="btn" style="left:160px;top:321px;width:141px;height:42px">Contact us</div>
</section>

<div class="abs about-back"></div>
<div class="abs about-photo" role="img" aria-label="Photo of a bronze Lady Justice statue beside a judge's gavel"></div>
<h2 class="abs serif about-title">ABOUT CORVELL</h2>
<p class="abs about-copy">Our small, skilled team is committed to the delivery of quality legal services to our clients.<br>Morillaqua Corvell originated with the legal practice founded by Mr Lucien Marcel Morillaqua in the 1940s. Today, we are a progressive law firm that has embraced both the traditional approach of our predecessor firms and the efficiencies of modern technology.<br>All of our services are available in English or in French according to the needs of our clients.</p>
<ul class="abs check-list">
  <li><svg width="13" height="13" viewBox="0 0 13 13"><rect x="1" y="2" width="10" height="10" rx="2" fill="none" stroke="#f7891f" stroke-width="1.5"/><path d="M3.5 6.5l2.5 2.5 6-7" fill="none" stroke="#f7891f" stroke-width="1.6"/></svg>Mission statement.</li>
  <li><svg width="13" height="13" viewBox="0 0 13 13"><rect x="1" y="2" width="10" height="10" rx="2" fill="none" stroke="#f7891f" stroke-width="1.5"/><path d="M3.5 6.5l2.5 2.5 6-7" fill="none" stroke="#f7891f" stroke-width="1.6"/></svg>Elodie Corvell.</li>
  <li><svg width="13" height="13" viewBox="0 0 13 13"><rect x="1" y="2" width="10" height="10" rx="2" fill="none" stroke="#f7891f" stroke-width="1.5"/><path d="M3.5 6.5l2.5 2.5 6-7" fill="none" stroke="#f7891f" stroke-width="1.6"/></svg>History.</li>
  <li><svg width="13" height="13" viewBox="0 0 13 13"><rect x="1" y="2" width="10" height="10" rx="2" fill="none" stroke="#f7891f" stroke-width="1.5"/><path d="M3.5 6.5l2.5 2.5 6-7" fill="none" stroke="#f7891f" stroke-width="1.6"/></svg>Location.</li>
</ul>
<div class="btn" style="left:608px;top:958px;width:114px;height:32px">Read more</div>

<div class="feature" style="left:160px">
  <svg width="50" height="48" viewBox="0 0 50 48" fill="none" stroke="#6b4a3a" stroke-width="1.6"><path d="M3 14L25 3l22 11z"/><path d="M5 16h40M5 40h40M2 45h46"/><path d="M10 19v18M17 19v18M25 19v18M33 19v18M40 19v18"/></svg>
  <h3>Winning Award Law Firm</h3>
  <p>Lawyers and attorneys act as both legal advisors and advocates, guiding individuals and businesses through intricate legal processes.</p>
  <div class="read-more">READ MORE <svg width="14" height="8" viewBox="0 0 14 8"><path d="M0 4h12M9 1l3 3-3 3" stroke="#f7891f" stroke-width="1.6" fill="none"/></svg></div>
</div>
<div class="feature" style="left:477px">
  <svg width="48" height="48" viewBox="0 0 48 48" fill="none" stroke="#6b4a3a" stroke-width="1.6"><path d="M4 3h26l6 6v36H4z"/><path d="M10 30h16M10 36h20M10 12h10M10 18h8"/><path d="M24 28L44 10l3 3-20 18-5 1z"/></svg>
  <h3>Confidential</h3>
  <p>Lawyers and attorneys act as both legal advisors and advocates, guiding individuals and businesses through intricate legal processes.</p>
  <div class="read-more">READ MORE <svg width="14" height="8" viewBox="0 0 14 8"><path d="M0 4h12M9 1l3 3-3 3" stroke="#f7891f" stroke-width="1.6" fill="none"/></svg></div>
</div>
<div class="feature" style="left:792px">
  <svg width="48" height="48" viewBox="0 0 48 48" fill="none" stroke="#6b4a3a" stroke-width="1.6"><path d="M24 3v38M14 45h20M18 41h12M6 10h36"/><path d="M10 10L3 26h14zM38 10l-7 16h14z"/><path d="M3 26a7 5 0 0 0 14 0M31 26a7 5 0 0 0 14 0"/></svg>
  <h3>Legal Protection</h3>
  <p>Lawyers and attorneys act as both legal advisors and advocates, guiding individuals and businesses through intricate legal processes.</p>
  <div class="read-more">READ MORE <svg width="14" height="8" viewBox="0 0 14 8"><path d="M0 4h12M9 1l3 3-3 3" stroke="#f7891f" stroke-width="1.6" fill="none"/></svg></div>
</div>

<section class="abs practice" role="img" aria-label="Faint background image of a Lady Justice statue and hanging scales"></section>
<div class="practice-center eyebrow" style="top:1370px">Our Expertise</div>
<h2 class="practice-center serif practice-title" style="top:1390px">LEGAL PRACTICE AREAS</h2>

<div class="area-card" style="left:160px">
  <div class="area-photo" role="img" aria-label="Photo of a lawyer signing papers beside a small building model" style="background:linear-gradient(135deg,#e8e6e3 0%,#9a9a9a 50%,#2e2e30 100%)"></div>
  <h4>Property law</h4>
  <div class="read-more">READ MORE <svg width="14" height="8" viewBox="0 0 14 8"><path d="M0 4h12M9 1l3 3-3 3" stroke="#f7891f" stroke-width="1.6" fill="none"/></svg></div>
</div>
<div class="area-card" style="left:460px">
  <div class="area-photo" role="img" aria-label="Photo of two business people shaking hands in an office" style="background:linear-gradient(135deg,#cfd6c4 0%,#eeeeea 40%,#4a4a4e 100%)"></div>
  <h4>Sale of Business</h4>
  <div class="read-more">READ MORE <svg width="14" height="8" viewBox="0 0 14 8"><path d="M0 4h12M9 1l3 3-3 3" stroke="#f7891f" stroke-width="1.6" fill="none"/></svg></div>
</div>
<div class="area-card" style="left:760px">
  <div class="area-photo" role="img" aria-label="Photo of an adviser reviewing documents with an elderly client" style="background:linear-gradient(135deg,#a9b597 0%,#e8e2d8 45%,#9bc26a 100%)"></div>
  <h4>Elder Law</h4>
  <div class="read-more">READ MORE <svg width="14" height="8" viewBox="0 0 14 8"><path d="M0 4h12M9 1l3 3-3 3" stroke="#f7891f" stroke-width="1.6" fill="none"/></svg></div>
</div>

<div class="abs stats-shadow"></div>
<div class="abs stats">
  <div class="stat"><b>1000+</b><span>Client Consultations</span></div>
  <div class="stat"><b>95%</b><span>Successful Cases</span></div>
  <div class="stat"><b>10m</b><span>Recovered cost for clients</span></div>
  <div class="stat"><b>30+</b><span>Professional Attorneys</span></div>
  <div class="view-more">VIEW MORE</div>
</div>

<div class="abs eyebrow" style="left:160px;top:2014px">History</div>
<h2 class="abs serif history-title">MORILLAQUA CORVELL</h2>
<div class="abs history-copy">
  <p>Morillaqua Corvell is a successor to the legal practice founded by Mr Lucien Marcel Morillaqua in the 1940s. Its various transformations saw Mr Lucien Marcel Morillaqua and his sons work in partnership with other lawyers prior to forming a smaller family firm (Morillaqua &amp; Morillaqua) on their own.</p>
  <p>The firm name was changed to “Morillaqua” when Martin Morillaqua became sole proprietor of the firm in the late 1980s.</p>
  <p>After working as an employed Solicitor with Martin Morillaqua, Elodie Corvell became proprietor of the firm in 2004 and the name of the practice was changed to “Morillaqua Corvell”.</p>
</div>
<div class="btn" style="left:161px;top:2284px;width:114px;height:32px">Read more</div>
<div class="abs history-back"></div>
<div class="abs history-photo" role="img" aria-label="Portrait photo of the firm's principal solicitor in a dark blazer"></div>

<div class="abs eyebrow" style="left:0;width:1200px;text-align:center;top:2412px">Get in touch</div>
<h2 class="abs serif" style="left:0;width:1200px;text-align:center;top:2428px;font-size:34px;line-height:44px">CONTACT US</h2>

<div class="abs contact-card">
  <div class="contact-item" style="top:50px">
    <svg width="18" height="22" viewBox="0 0 18 22"><path d="M9 1a7 7 0 0 0-7 7c0 5 7 13 7 13s7-8 7-13a7 7 0 0 0-7-7z" fill="#fff"/><circle cx="9" cy="8" r="2.6" fill="#f7891f"/></svg>
    <div><strong>Address</strong><small>Level 9, 48 Harrow Lane Sydney, NSW<br>2000</small></div>
  </div>
  <div class="contact-item" style="top:133px">
    <svg width="20" height="20" viewBox="0 0 20 20"><path d="M4 1l4 4-2 3c1 3 3 5 6 6l3-2 4 4-3 3C8 19 1 12 1 4z" fill="#fff"/></svg>
    <div><strong>Phone</strong><small>(+612) 5550 1842</small></div>
  </div>
  <div class="contact-item" style="top:196px">
    <svg width="26" height="22" viewBox="0 0 26 22" fill="none" stroke="#fff" stroke-width="1.6"><rect x="6" y="1" width="14" height="7"/><rect x="1" y="8" width="24" height="10" rx="2"/><rect x="6" y="14" width="14" height="7"/></svg>
    <div><strong>Fax</strong><small>(+612) 5550 1843</small></div>
  </div>
  <div class="contact-item" style="top:257px">
    <svg width="20" height="16" viewBox="0 0 20 16"><rect x="0" y="1" width="20" height="14" rx="1" fill="#fff"/><path d="M1 2l9 7 9-7" fill="none" stroke="#f7891f" stroke-width="1.6"/></svg>
    <div><strong>Email</strong><small>elodie@corvell.com.au</small></div>
  </div>
</div>

<p class="abs form-intro">Lorem ipsum dolor sit amet, consectetur adipiscing elit. Sed tincidunt nisi a turpis interdum consequat. Pellentesque ut semper</p>
<span class="field-label" style="left:515px;top:2574px">Name</span>
<span class="field-label" style="left:781px;top:2574px">EMail</span>
<div class="field" style="left:515px;top:2594px;width:259px;height:36px"></div>
<div class="field" style="left:781px;top:2594px;width:259px;height:36px"></div>
<span class="field-label" style="left:515px;top:2642px">Phone</span>
<div class="field" style="left:515px;top:2663px;width:525px;height:36px"></div>
<span class="field-label" style="left:515px;top:2711px">Message</span>
<div class="field" style="left:515px;top:2731px;width:525px;height:60px"></div>
<div class="btn" style="left:517px;top:2809px;width:126px;height:32px">Submit</div>

<footer class="abs footer"></footer>
<div class="social" aria-label="Social media links">
  <span></span><span></span><span></span><span></span>
</div>
<nav class="footer-nav">
  <span class="active">HOME</span><span>OUR SERVICES</span><span>DOWNLOAD</span><span>CONTACT US</span><span>LINKS</span>
</nav>
<div class="abs legal">© 2024 MORILLAQUA CORVELL | ALL RIGHT RESERVED.</div>

</body>
</html>
```